Dessert and wine restaurant.

I am a starter restaurant. My concept for my restaurant is to serve made from scratch desserts and wine and beer selections. My thoughts are that after dinner at your favorite restaurant you will c ome to enjoy a fantastic dessert and a glass of wine or beer. Entertainment will also be a part of the Quorlane experience. By the way the name of my restaurant is Quorlane why quorlane? It will be an experience of indulgence in the finest made from scratch desserts.

Target Market(s)

Anyone looking for a delicious, decadent dessert and a glass of wine or beer. Also coffees and tea.

Industry/Entity Type

Restaurant

Logo Text

dessert on a plate with a glass of wine. Or just give me your design ideas Im open.

Font styles to use
Decorative
Script

Colors
0455a3
5c5c5c
aaaaaa
ec2027

Requirements
Must have
• dessert Ideas
Nice to have
• elegant ideas. Contemporary.

```html
<!DOCTYPE html>
<html lang="en">
<head>
<meta charset="utf-8">
<title>Quorlane Dessert Menu</title>
<link rel="stylesheet" href="https://fonts.googleapis.com/css2?family=Arimo:ital,wght@0,400;0,700;1,400&family=Kaushan+Script&display=swap">
<style>
:root{
  --stage:#d6d6d6;
  --ink:#1c1c1c;
  --price:#ec2027;
  --heading:#c8262c;
  --brand:#0455a3;
  --band:#111111;
  --paper-top:#f29a62;
  --paper-mid:#f6c98a;
  --paper-bottom:#fbe9ad;
  --photo-a:#f3e3cf;
  --photo-b:#d9534f;
  --photo-c:#f6d7c4;
  --swoosh:#ffffff;
  --footer-text:#ffffff;
}
*{box-sizing:border-box;margin:0;padding:0}
html,body{width:1200px;height:799px;overflow:hidden}
body{background:var(--stage);font-family:"Arimo",Arial,sans-serif;position:relative}

.menu{
  position:absolute;top:14px;width:333px;height:772px;overflow:hidden;
  background:linear-gradient(180deg,var(--paper-top) 22%,var(--paper-mid) 45%,var(--paper-bottom) 80%);
  box-shadow:0 6px 18px rgba(0,0,0,.35);
  color:var(--ink);
}
.menu--front{left:247px}
.menu--back{
  left:620px;
  --price:#6b6b6b;
  --heading:#8a8a8a;
  --brand:#3c3c3c;
  --paper-top:#e8e8e8;
  --paper-mid:#f6f6f6;
  --paper-bottom:#ffffff;
  --photo-a:#f0f0f0;
  --photo-b:#9a9a9a;
  --photo-c:#d8d8d8;
  --band:#ffffff;
  --footer-text:#5c5c5c;
}

.menu__photo{
  position:absolute;left:0;top:0;width:100%;height:170px;
  background:linear-gradient(100deg,var(--photo-b) 0%,var(--photo-a) 35%,var(--photo-c) 65%,var(--photo-b) 100%);
}
.menu__swoosh{position:absolute;left:0;top:118px;width:100%;height:70px}

.brand{
  position:absolute;left:50%;top:64px;transform:translateX(-50%);
  display:flex;align-items:center;gap:8px;
  background:#ffffff;padding:8px 16px;border-radius:4px;
}
.brand__mark{width:12px;height:12px;background:var(--brand)}
.brand__name{font-weight:700;font-size:22px;color:var(--brand);letter-spacing:.5px}

.meals{
  position:absolute;left:42px;top:160px;width:250px;height:22px;border-radius:11px;
  background:#1a1a1a;color:#fff;font-size:9px;font-weight:700;letter-spacing:.8px;
  display:flex;align-items:center;justify-content:center;gap:8px;
}
.meals__dot{width:5px;height:5px;background:#fff;transform:rotate(45deg)}

.section-title{
  position:absolute;left:0;width:100%;text-align:center;
  font-family:"Kaushan Script",cursive;font-size:17px;color:var(--heading);
}
.section-title::after{
  content:"";display:block;width:110px;height:1px;margin:2px auto 0;
  background:linear-gradient(90deg,transparent,var(--heading),transparent);
}
.section-title--dessert{top:205px}
.section-title--plates{top:492px}

.columns{position:absolute;left:20px;width:300px;display:grid;grid-template-columns:1fr 1fr;column-gap:12px}
.columns--dessert{top:244px}
.columns--plates{top:530px}
.col{display:flex;flex-direction:column;gap:5px}

.item{display:grid;grid-template-columns:10px 1fr auto;column-gap:5px;align-items:start;font-size:8.4px;font-weight:700;line-height:1.15}
.item__box{width:7px;height:7px;border:1px solid #333;background:#fff;margin-top:2px}
.item__price{color:var(--price);font-size:8px}
.item__note{display:block;font-weight:400;font-style:italic;font-size:6.6px;line-height:1.15}
.item__note--inline{display:inline}
.item--option{margin-left:14px}

.tagline{
  position:absolute;left:0;top:712px;width:100%;text-align:center;
  font-family:"Kaushan Script",cursive;font-size:12px;line-height:1.2;color:#2a2a2a;
}
.footer{
  position:absolute;left:0;bottom:0;width:100%;height:28px;background:var(--band);
  display:flex;align-items:center;justify-content:center;gap:36px;
  color:var(--footer-text);font-size:9px;font-weight:700;
}
.footer__entry{display:flex;align-items:center;gap:5px}
.footer__icon{width:10px;height:10px}
.menu--back .tagline{visibility:hidden}
.menu--back .footer{border-top:1px solid #bbbbbb}
</style>
</head>
<body>

<article class="menu menu--front">
  <div class="menu__photo" role="img" aria-label="Photo of fruit tarts, strawberry desserts and poured red wine"></div>
  <svg class="menu__swoosh" viewBox="0 0 333 70" preserveAspectRatio="none" aria-hidden="true">
    <path d="M0 52 Q166 0 333 52 L333 70 L0 70 Z" fill="var(--paper-top)"/>
    <path d="M0 52 Q166 0 333 52" fill="none" stroke="var(--swoosh)" stroke-width="4"/>
    <path d="M0 58 Q166 8 333 58" fill="none" stroke="#2a2a2a" stroke-width="2"/>
  </svg>
  <div class="brand"><span class="brand__mark"></span><span class="brand__name">Quorlane</span></div>
  <div class="meals">LUNCH <span class="meals__dot"></span> DINNER <span class="meals__dot"></span> LATE NIGHT</div>

  <h2 class="section-title section-title--dessert">Dessert</h2>
  <div class="columns columns--dessert">
    <div class="col">
      <div class="item"><span class="item__box"></span><span>Lemon<br>pound cake</span><span class="item__price">$2.5</span></div>
      <div class="item"><span class="item__box"></span><span>Amaretto<br>chocolate pound cake</span><span class="item__price">$2.5</span></div>
      <div class="item"><span class="item__box"></span><span>Vanilla-almond<br>pound cake</span><span class="item__price">$2.5</span></div>
      <div class="item"><span class="item__box"></span><span>Crumbly</span><span class="item__price">$2.5</span></div>
      <div class="item"><span class="item__box"></span><span>Buttery apple-pie</span><span class="item__price">$2.5</span></div>
      <div class="item"><span class="item__box"></span><span>Pecan pie</span><span class="item__price">$2.5</span></div>
      <div class="item"><span class="item__box"></span><span>Salted</span><span class="item__price">$2.5</span></div>
      <div class="item"><span class="item__box"></span><span>Carmel<br>pecan cheesecake</span><span class="item__price">$2.5</span></div>
      <div class="item"><span></span><span>Traditional<br>cheesecake <span class="item__note item__note--inline">(with toppings)</span></span><span class="item__price">$2.5</span></div>
      <div class="item item--option"><span class="item__box"></span><span>strawberry</span><span></span></div>
      <div class="item item--option"><span class="item__box"></span><span>blueberry</span><span></span></div>
      <div class="item item--option"><span class="item__box"></span><span>cherry</span><span></span></div>
    </div>
    <div class="col">
      <div class="item"><span class="item__box"></span><span>Cupcake minis</span><span class="item__price">$2.5</span></div>
      <div class="item"><span class="item__box"></span><span>Coconut cream pie</span><span class="item__price">$2.5</span></div>
      <div class="item"><span class="item__box"></span><span>Chocolate-chip cookies<span class="item__note">(Hot out of the oven)</span></span><span class="item__price">$2.5</span></div>
      <div class="item"><span class="item__box"></span><span>Chocolate cookies</span><span class="item__price">$2.5</span></div>
      <div class="item"><span class="item__box"></span><span>Peanut butter cookies</span><span class="item__price">$2.5</span></div>
      <div class="item"><span class="item__box"></span><span>Oatmeal raisin cookies</span><span class="item__price">$2.5</span></div>
      <div class="item"><span class="item__box"></span><span>Louisiana style bread</span><span class="item__price">$2.5</span></div>
      <div class="item"><span></span><span>Puddin with Rum sauce</span><span class="item__price">$2.5</span></div>
    </div>
  </div>

  <h2 class="section-title section-title--plates">Small Plate Item</h2>
  <div class="columns columns--plates">
    <div class="col">
      <div class="item"><span class="item__box"></span><span>Guacamole<span class="item__note">on a bed of lettuce with toasted olive oil and garlic tortilla triangles</span></span><span class="item__price">$2.5</span></div>
      <div class="item"><span class="item__box"></span><span>Jerk<span class="item__note">wings with celery and carrot sticks</span></span><span class="item__price">$2.5</span></div>
      <div class="item"><span class="item__box"></span><span>Jumbo Lump<span class="item__note">mini crabcakes with special sauce</span></span><span class="item__price">$2.5</span></div>
      <div class="item"><span class="item__box"></span><span>Cheesy Spinach<span class="item__note">and artichoke dip with toasted olive oil and garlic tortilla triangles</span></span><span class="item__price">$2.5</span></div>
    </div>
    <div class="col">
      <div class="item"><span class="item__box"></span><span>Shrimp escargot<span class="item__note">with butter garlic sauce and cheesy French baguette toast</span></span><span class="item__price">$2.5</span></div>
      <div class="item"><span class="item__box"></span><span>Juicy turkey<span class="item__note">meatballs with Asian sauce</span></span><span class="item__price">$2.5</span></div>
      <div class="item"><span class="item__box"></span><span>Internationally hand<span class="item__note">selected cheese plate with fruit</span></span><span class="item__price">$2.5</span></div>
      <div class="item"><span class="item__box"></span><span>Nuts and selected crackers</span><span class="item__price">$2.5</span></div>
    </div>
  </div>

  <p class="tagline">Quorlane a delightful place for delicious,<br>indulgent desserts...</p>
  <footer class="footer">
    <span class="footer__entry"><svg class="footer__icon" viewBox="0 0 10 10" aria-hidden="true"><rect x="0.5" y="2" width="9" height="6.5" fill="none" stroke="currentColor"/><path d="M0.5 2 L5 6 L9.5 2" fill="none" stroke="currentColor"/></svg>email@quorlane.com</span>
    <span class="footer__entry"><svg class="footer__icon" viewBox="0 0 10 10" aria-hidden="true"><path d="M2 1 L4 1 L4.6 3.4 L3.3 4.3 Q4.3 6.3 5.7 6.7 L6.6 5.4 L9 6 L9 8 Q5 9.5 1 4 Z" fill="currentColor"/></svg>555-0142-77</span>
  </footer>
</article>

<article class="menu menu--back">
  <div class="menu__photo" role="img" aria-label="Black and white photo of fruit tarts, desserts and poured wine"></div>
  <svg class="menu__swoosh" viewBox="0 0 333 70" preserveAspectRatio="none" aria-hidden="true">
    <path d="M0 52 Q166 0 333 52 L333 70 L0 70 Z" fill="var(--paper-top)"/>
    <path d="M0 52 Q166 0 333 52" fill="none" stroke="#ffffff" stroke-width="4"/>
    <path d="M0 58 Q166 8 333 58" fill="none" stroke="#2a2a2a" stroke-width="2"/>
  </svg>
  <div class="brand"><span class="brand__mark"></span><span class="brand__name">Quorlane</span></div>
  <div class="meals">LUNCH <span class="meals__dot"></span> DINNER <span class="meals__dot"></span> LATE NIGHT</div>

  <h2 class="section-title section-title--dessert">Dessert</h2>
  <div class="columns columns--dessert">
    <div class="col">
      <div class="item"><span class="item__box"></span><span>Lemon<br>pound cake</span><span class="item__price">$2.5</span></div>
      <div class="item"><span class="item__box"></span><span>Amaretto<br>chocolate pound cake</span><span class="item__price">$2.5</span></div>
      <div class="item"><span class="item__box"></span><span>Vanilla-almond<br>pound cake</span><span class="item__price">$2.5</span></div>
      <div class="item"><span class="item__box"></span><span>Crumbly</span><span class="item__price">$2.5</span></div>
      <div class="item"><span class="item__box"></span><span>Buttery apple-pie</span><span class="item__price">$2.5</span></div>
      <div class="item"><span class="item__box"></span><span>Pecan pie</span><span class="item__price">$2.5</span></div>
      <div class="item"><span class="item__box"></span><span>Salted</span><span class="item__price">$2.5</span></div>
      <div class="item"><span class="item__box"></span><span>Carmel<br>pecan cheesecake</span><span class="item__price">$2.5</span></div>
      <div class="item"><span></span><span>Traditional<br>cheesecake <span class="item__note item__note--inline">(with toppings)</span></span><span class="item__price">$2.5</span></div>
      <div class="item item--option"><span class="item__box"></span><span>strawberry</span><span></span></div>
      <div class="item item--option"><span class="item__box"></span><span>blueberry</span><span></span></div>
      <div class="item item--option"><span class="item__box"></span><span>cherry</span><span></span></div>
    </div>
    <div class="col">
      <div class="item"><span class="item__box"></span><span>Cupcake minis</span><span class="item__price">$2.5</span></div>
      <div class="item"><span class="item__box"></span><span>Coconut cream pie</span><span class="item__price">$2.5</span></div>
      <div class="item"><span class="item__box"></span><span>Chocolate-chip cookies<span class="item__note">(Hot out of the oven)</span></span><span class="item__price">$2.5</span></div>
      <div class="item"><span class="item__box"></span><span>Chocolate cookies</span><span class="item__price">$2.5</span></div>
      <div class="item"><span class="item__box"></span><span>Peanut butter cookies</span><span class="item__price">$2.5</span></div>
      <div class="item"><span class="item__box"></span><span>Oatmeal raisin cookies</span><span class="item__price">$2.5</span></div>
      <div class="item"><span class="item__box"></span><span>Louisiana style bread</span><span class="item__price">$2.5</span></div>
      <div class="item"><span></span><span>Puddin with Rum sauce</span><span class="item__price">$2.5</span></div>
    </div>
  </div>

  <h2 class="section-title section-title--plates">Small Plate Item</h2>
  <div class="columns columns--plates">
    <div class="col">
      <div class="item"><span class="item__box"></span><span>Guacamole<span class="item__note">on a bed of lettuce with toasted olive oil and garlic tortilla triangles</span></span><span class="item__price">$2.5</span></div>
      <div class="item"><span class="item__box"></span><span>Jerk<span class="item__note">wings with celery and carrot sticks</span></span><span class="item__price">$2.5</span></div>
      <div class="item"><span class="item__box"></span><span>Jumbo Lump<span class="item__note">mini crabcakes with special sauce</span></span><span class="item__price">$2.5</span></div>
      <div class="item"><span class="item__box"></span><span>Cheesy Spinach<span class="item__note">and artichoke dip with toasted olive oil and garlic tortilla triangles</span></span><span class="item__price">$2.5</span></div>
    </div>
    <div class="col">
      <div class="item"><span class="item__box"></span><span>Shrimp escargot<span class="item__note">with butter garlic sauce and cheesy French baguette toast</span></span><span class="item__price">$2.5</span></div>
      <div class="item"><span class="item__box"></span><span>Juicy turkey<span class="item__note">meatballs with Asian sauce</span></span><span class="item__price">$2.5</span></div>
      <div class="item"><span class="item__box"></span><span>Internationally hand<span class="item__note">selected cheese plate with fruit</span></span><span class="item__price">$2.5</span></div>
      <div class="item"><span class="item__box"></span><span>Nuts and selected crackers</span><span class="item__price">$2.5</span></div>
    </div>
  </div>

  <p class="tagline">Quorlane a delightful place for delicious,<br>indulgent desserts...</p>
  <footer class="footer"></footer>
</article>

</body>
</html>
```